Thistleby's Organic's. I make and sell organic bath & body products. Nourishing bath & body products. Products are soaps, scrubs, lip balms, bath salts, baby & mother products (belly balm, nipple balm, diaper balm, baby bath soak, chest rub,) . I use botanical and or herbs in all my recipes. I create my own recipes. I like muted colors...but I would like something that will get your attention. I like the colors green and brown, but open to any other colors. I would also like to get information about labels (different sizes for my products) I do like the pasley print and maybe even a cute owl.

Target Market(s)

women, pregnant and nursing women, women with children and men

Industry/Entity Type

Baby

Contact Information for Business Card

Rhoda Quillmore
527-614-2870,rquillmore@lumaweb.net
rquillmore@lumaweb.net

Font styles to use
Other font styles liked:
• bree

Requirements
Must have
• Thistleby's Organic's, nourishing bath & body products. It needs to get a person attention. I would like to see cards that are hip and fun. I would also like to view cards that are classy. I do like muted colors but I do have an open mind (use any color you think would be right) So far a lot of the cards have had leaves....I really do not like that design.
Nice to have
• ???pasley in the background ?cute owl
Should not have
• leaves

```html
<!DOCTYPE html>
<html lang="en">
<head>
<meta charset="utf-8">
<title>Thistleby's Organic's – Business Card</title>
<link rel="stylesheet" href="https://fonts.googleapis.com/css2?family=Pinyon+Script&family=Arimo&display=swap">
<style>
  :root {
    --stage: #e9e6e2;
    --card-red: #d9264a;
    --card-red-light: #e42f55;
    --ink-white: #ffffff;
    --ornament-tint: rgba(255, 255, 255, 0.38);
  }
  html, body {
    margin: 0;
    padding: 0;
    width: 1200px;
    height: 885px;
    overflow: hidden;
    background: var(--stage);
  }
  .canvas {
    position: relative;
    width: 1200px;
    height: 885px;
    display: flex;
    align-items: center;
    justify-content: center;
  }
  .business-card {
    position: relative;
    width: 900px;
    height: 514px;
    background: radial-gradient(ellipse at 50% 40%, var(--card-red-light), var(--card-red));
    box-shadow: 0 6px 24px rgba(0, 0, 0, 0.18);
  }
  .card-frame {
    position: absolute;
    inset: 0;
  }
  .corner-ornament {
    position: absolute;
    width: 96px;
    height: 96px;
    background: var(--ornament-tint);
    border-radius: 8px;
  }
  .corner-ornament.top-left { top: 22px; left: 22px; }
  .corner-ornament.top-right { top: 22px; right: 22px; }
  .corner-ornament.bottom-left { bottom: 22px; left: 22px; }
  .corner-ornament.bottom-right { bottom: 22px; right: 22px; }
  .card-content {
    position: absolute;
    inset: 0;
    display: flex;
    flex-direction: column;
    align-items: center;
    justify-content: center;
    color: var(--ink-white);
    text-align: center;
    padding-top: 30px;
  }
  .brand-name {
    margin: 0 0 14px;
    font-family: "Pinyon Script", cursive;
    font-weight: 400;
    font-size: 78px;
    line-height: 1;
    letter-spacing: 2px;
  }
  .contact-line {
    margin: 0;
    font-family: "Arimo", Arial, sans-serif;
    font-size: 30px;
    line-height: 1.2;
  }
</style>
</head>
<body>
  <div class="canvas">
    <section class="business-card" aria-label="Thistleby's Organic's business card">
      <svg class="card-frame" width="900" height="514" viewBox="0 0 900 514" aria-hidden="true">
        <rect x="42" y="42" width="816" height="430" fill="none" stroke="#ffffff" stroke-width="2.5"/>
      </svg>
      <div class="corner-ornament top-left" role="img" aria-label="White scrolled filigree corner ornament"></div>
      <div class="corner-ornament top-right" role="img" aria-label="White scrolled filigree corner ornament"></div>
      <div class="corner-ornament bottom-left" role="img" aria-label="White scrolled filigree corner ornament"></div>
      <div class="corner-ornament bottom-right" role="img" aria-label="White scrolled filigree corner ornament"></div>
      <div class="card-content">
        <h1 class="brand-name">Thistleby's Organic's</h1>
        <p class="contact-line">rquillmore@lumaweb.net</p>
        <p class="contact-line">527-614-2870</p>
      </div>
    </section>
  </div>
</body>
</html>
```